Hi-Tech looking WordPress design for Bright Lane Technologies

We are looking for a creative WordPress design for our client Bright Lane who is a Valtreno copier and printer managed services distributer. They also provide managed IT services.

Target Market(s)

Businesses with 10+ employees

Industry/Entity Type

Printer

Number of Pages Required

1 page

Font styles to use
Sans Serif

Requirements
Must have
• My client distributes and manages Valtreno printers and copy machines to many business industries. They also manage IT network services so their site needs to be hi-tech looking. Their corporate color is Pantone 354C and I've attached their logo.
Nice to have
• A user friendly interface with a top level menu and sliders that will market their services.
Should not have
• Do NOT display the Valtreno logo in their design.

```html
<!DOCTYPE html>
<html lang="en">
<head>
<meta charset="utf-8">
<title>Bright Lane Technologies</title>
<link href="https://fonts.googleapis.com/css2?family=Roboto:wght@300;400;500;700;900&family=Roboto+Slab:wght@300;700&display=swap" rel="stylesheet">
<style>
:root{
  --green:#27953f;
  --green-dark:#1f7a33;
  --green-light:#3fb55a;
  --ink:#1b1b1b;
  --hero:#232323;
  --grey-bg:#efefef;
  --text:#777;
  --white:#fff;
}
*{margin:0;padding:0;box-sizing:border-box}
html,body{width:820px;height:1200px;overflow:hidden}
body{position:relative;font-family:'Roboto',sans-serif;background:var(--white);color:var(--text)}
.abs{position:absolute}
.top-strip{left:0;top:0;width:820px;height:4px;background:#333}
.brand{left:132px;top:17px;display:flex;align-items:center;gap:7px;color:var(--green);font-size:26px;font-weight:400}
.brand-dot{width:34px;height:34px;border-radius:50%;background:var(--green)}
.social-top{left:494px;top:28px;display:flex;gap:8px}
.social-top span{width:14px;height:14px;border-radius:50%;background:#9a9a9a}
.phone{left:569px;top:20px;width:129px;height:30px;background:#3a3a3a;display:flex;align-items:center;color:var(--white);font-size:14px;font-weight:500}
.phone .ico{width:32px;height:30px;background:var(--green-dark);display:flex;align-items:center;justify-content:center;margin-right:9px}
.nav{left:0;top:62px;width:820px;height:30px;background:linear-gradient(#2ea347,var(--green-dark))}
.nav ul{list-style:none;display:flex;position:absolute;left:120px;top:0;height:30px}
.nav li{color:var(--white);font-size:8.5px;font-weight:500;padding:0 11px;line-height:30px;border-right:1px solid rgba(0,0,0,.18)}
.nav li.current{background:#2d2d2d;padding:0 15px}
.nav li:last-child{border-right:0}
.hero{left:0;top:92px;width:820px;height:284px;background:radial-gradient(circle at 60% 45%,#3b3b3b,var(--hero) 70%)}
.hero h1{position:absolute;left:148px;top:84px;font-family:'Roboto Slab',serif;font-weight:300;font-size:25px;line-height:32px;color:#e8e8e8}
.hero h1 b{font-weight:700;color:var(--white)}
.btn{position:absolute;left:148px;top:167px;width:98px;height:35px;background:var(--green);color:var(--white);font-size:11px;line-height:35px;text-align:center;border-radius:2px}
.hero-media{position:absolute;left:432px;top:36px;width:236px;height:216px;background:radial-gradient(#f4f4f4,#c9c9c9);border-radius:4px}
.arrow{position:absolute;top:120px}
.band{left:0;top:376px;width:820px;height:56px;background:var(--green);color:#e9f6ec;font-size:11.5px;text-align:center;line-height:18px;padding-top:10px;font-weight:300}
.band b{color:var(--ink);font-weight:700}
.band-tip{left:401px;top:431px;width:0;height:0;border-left:9px solid transparent;border-right:9px solid transparent;border-top:8px solid var(--green)}
.card{top:486px;width:116px;height:298px;border-radius:58px;background:linear-gradient(160deg,var(--green-light),var(--green) 60%,var(--green-dark));overflow:hidden}
.card-head{position:absolute;left:6px;top:6px;width:104px;height:104px;border-radius:50%;background:var(--white);display:flex;flex-direction:column;align-items:center;justify-content:center;color:#444;text-align:center;line-height:1.05}
.card-head .big{font-weight:900;font-size:20px;color:#333}
.card-head .sm{font-size:11px;font-weight:300}
.card p{position:absolute;left:14px;top:129px;width:88px;text-align:center;color:var(--white);font-size:8.3px;line-height:13.8px}
.card svg{position:absolute;left:44px;top:250px}
.welcome{left:0;top:829px;width:820px;height:287px;background:linear-gradient(var(--grey-bg),#f7f7f7)}
.welcome-media{position:absolute;left:168px;top:35px;width:212px;height:208px;background:radial-gradient(#fafafa,#cfcfcf);border-radius:8px}
.welcome-text{position:absolute;left:428px;top:56px;width:250px}
.welcome-text h2{font-family:'Roboto Slab',serif;font-size:22px;font-weight:300;color:#444;margin-bottom:12px}
.welcome-text h2 b{font-weight:700}
.welcome-text p{font-size:8.3px;line-height:12.8px;margin-bottom:12px}
.welcome-text p b{color:#333;font-weight:500}
.welcome-text .accent{color:var(--green);font-weight:500}
.footer-line{left:0;top:1116px;width:820px;height:4px;background:var(--green)}
.footer{left:0;top:1120px;width:820px;height:80px;background:var(--ink);text-align:center;color:#aaa;font-size:7.5px}
.footer .links{margin-top:15px}
.footer .links .on{color:var(--green)}
.footer .copy{margin-top:4px}
.footer .social{display:flex;justify-content:center;gap:6px;margin-top:13px}
.footer .social span{width:20px;height:20px;border-radius:50%;border:1px solid #666}
</style>
</head>
<body>
<div class="abs top-strip"></div>
<div class="abs brand"><span class="brand-dot"></span>Bright Lane</div>
<div class="abs social-top"><span></span><span></span><span></span></div>
<div class="abs phone"><span class="ico"><svg width="14" height="14" viewBox="0 0 24 24"><path fill="#fff" d="M6.6 10.8a15 15 0 0 0 6.6 6.6l2.2-2.2c.3-.3.7-.4 1-.2 1.1.4 2.3.6 3.6.6.6 0 1 .4 1 1V20c0 .6-.4 1-1 1A17 17 0 0 1 3 4c0-.6.4-1 1-1h3.5c.6 0 1 .4 1 1 0 1.3.2 2.5.6 3.6.1.3 0 .7-.2 1z"/></svg></span>555 010 4821</div>

<nav class="abs nav"><ul>
<li class="current">HOME</li><li>WHY US</li><li>PRODUCTS &amp; SERVICES</li><li>TESTIMONIALS</li><li>GREEN</li><li>NEWS</li><li>HELPING HANDS</li><li>CONTACT US</li>
</ul></nav>

<section class="abs hero">
<h1>Power Up your business.<br>Think <b>Bright Lane.</b></h1>
<div class="btn">KNOW MORE &gt;</div>
<div class="hero-media" role="img" aria-label="Large multifunction office copier"></div>
<svg class="arrow" style="left:18px" width="16" height="30" viewBox="0 0 16 30"><path d="M14 2 3 15l11 13" stroke="#666" stroke-width="3" fill="none"/></svg>
<svg class="arrow" style="left:786px" width="16" height="30" viewBox="0 0 16 30"><path d="M2 2l11 13L2 28" stroke="#666" stroke-width="3" fill="none"/></svg>
</section>

<div class="abs band">KANSAS CITY'S AWARD WINNING AND INDEPENDENTLY<br>OWNED OFFICE EQUIPMENT DEALER <b>SINCE 1993</b></div>
<div class="abs band-tip"></div>

<div class="abs card" style="left:172px">
<div class="card-head"><span class="big">Show</span><span class="sm">Me Your<br>Machine</span></div>
<p>Lorem ipsum dolor sit amet, consectetur adipisicing elit, sed do adipisicing elit, sed incididunt ut labore et adipisicing elit, sed do dolore magna aliqua.</p>
<svg width="28" height="26" viewBox="0 0 28 26"><path d="M4 24C4 12 10 8 18 8V2l9 9-9 9v-6c-6 0-10 2-14 10z" fill="#fff"/></svg>
</div>
<div class="abs card" style="left:350px">
<div class="card-head"><span class="sm">How to<br>Choose a</span><span class="big">Copier</span></div>
<p>Lorem ipsum dolor sit amet, consectetur adipisicing elit, sed do adipisicing elit, sed incididunt ut labore et adipisicing elit, sed do dolore magna aliqua.</p>
<svg width="28" height="26" viewBox="0 0 28 26"><path d="M4 24C4 12 10 8 18 8V2l9 9-9 9v-6c-6 0-10 2-14 10z" fill="#fff"/></svg>
</div>
<div class="abs card" style="left:530px">
<div class="card-head"><span class="big">Features</span><span class="sm">of Multifunctional<br>Devices</span></div>
<p>Lorem ipsum dolor sit amet, consectetur adipisicing elit, sed do adipisicing elit, sed incididunt ut labore et adipisicing elit, sed do dolore magna aliqua.</p>
<svg width="28" height="26" viewBox="0 0 28 26"><path d="M4 24C4 12 10 8 18 8V2l9 9-9 9v-6c-6 0-10 2-14 10z" fill="#fff"/></svg>
</div>

<section class="abs welcome">
<div class="welcome-media" role="img" aria-label="Desktop printer printing a colour page"></div>
<div class="welcome-text">
<h2><b>Welcome</b> to our site</h2>
<p>Bright Lane empowers Kansas City companies with <b>copiers</b>, <b>multi-functional printers</b> and <b>digital imaging equipment</b>.</p>
<p>It's really that simple. We bring our expertise to your business – simplifying your business' document management systems.</p>
<p>Find out how we can streamline your business with our complimentary <b>Managed Print Services</b>.</p>
<p><span class="accent">Make the switch to Bright Lane</span> and see how we can help your business thrive.</p>
</div>
</section>

<div class="abs footer-line"></div>
<footer class="abs footer">
<div class="links"><span class="on">Home</span> | Why Us | Services | Testimonials | GREEN | News | Helping Hands | Contact Us | Site Map</div>
<div class="copy">© Bright Lane Technologies, Inc. | 555.010.4821</div>
<div class="social"><span></span><span></span><span></span></div>
</footer>
</body>
</html>
```